a business advisory consulting website

I need a website 3-5 pages to sell my professional services in IT and Project management Consulting. My company name is Northwell Strategy Consulting. I want it to be device friendly and easy to navigate for the busy executive however intriguing enough.
I have attached some info I drafted on About the company and personal Bio. Also there is a website that I really like that I have attached the initial site pdf and websites that I like are here: https://quillmarshcapital.example, https://tandermoviews.example, https://www.felkinlearningconsulting.example as examples. Thanks
Updates

Hi Designers, I have uploaded the logo in 3D .png format, to assist in the web design.

Target Market(s)

B2B, governments, IT companies, Project Management companies and Consulting firms, small medium enterprises to large corporate enterprises.

Industry/Entity Type

It Professional

Coding

Coded - Design and coding required

Number of Pages Required

5+ page

Font styles to use
Sans Serif

Requirements
Must have
• Home, About company, the team, what we do and contact us
Nice to have
• Blog
Should not have
• pop ups, flash

```html
<!DOCTYPE html>
<html lang="en">
<head>
<meta charset="utf-8">
<title>Northwell Strategy Consulting</title>
<link href="https://fonts.googleapis.com/css2?family=Poppins:ital,wght@0,400;0,500;0,600;0,700;0,800;1,500&display=swap" rel="stylesheet">
<style>
:root{
  --navy:#262c4c;
  --red:#e3262a;
  --ink:#2a2f45;
  --muted:#6c7080;
  --line:#e3e3e8;
  --soft:#f3f3f4;
  --white:#ffffff;
}
*{margin:0;padding:0;box-sizing:border-box}
html,body{width:1200px;height:4563px;overflow:hidden}
body{position:relative;font-family:'Poppins',sans-serif;color:var(--ink);background:var(--white)}
.abs{position:absolute}
.center{left:0;width:1200px;text-align:center}
.btn{position:absolute;z-index:3;background:var(--red);color:var(--white);border-radius:22px;font-weight:600;font-size:14px;display:flex;align-items:center;justify-content:center;letter-spacing:.3px}
.red{color:var(--red)}
/* header */
.brand{position:absolute;left:163px;top:26px;display:flex;align-items:center;gap:8px;font-weight:700;font-size:19px;color:var(--navy);line-height:1}
.brand .mark{width:14px;height:14px;background:var(--red)}
.nav{position:absolute;left:404px;top:40px;display:flex;gap:21px;font-size:11px;font-weight:500;color:var(--navy)}
.nav .active{color:var(--red)}
.call{position:absolute;left:881px;top:24px;display:flex;gap:10px;align-items:center}
.call small{display:block;font-size:9px;font-weight:600;color:var(--navy)}
.call b{font-size:17px;color:var(--red);font-weight:600}
/* hero */
.hero-kicker{top:144px;font-size:22px;font-weight:600;color:var(--red);z-index:2}
.hero-title{top:180px;font-size:46px;font-weight:800;line-height:50px;color:var(--navy);letter-spacing:.5px;z-index:2}
.hero-sub{top:287px;font-size:13.5px;color:var(--navy);z-index:2}
.meeting{position:absolute;z-index:1;left:385px;top:346px;width:420px;height:420px;border-radius:50%;border:1px solid #f0a3a4;background:radial-gradient(circle,#f4f6f8 0%,#e9eef2 55%,#fff 72%)}
.socials{position:absolute;left:163px;top:774px;display:flex;gap:10px}
.socials i{width:10px;height:10px;border-radius:50%;background:var(--white);display:block}
.dashes{position:absolute;left:257px;top:779px;display:flex;gap:6px}
.dashes i{display:block;width:28px;height:2px;background:#4b5170}
.dashes i:first-child{background:var(--red)}
.welcome{color:var(--white)}
.welcome .to{top:853px;font-size:15px;font-weight:500}
.welcome .name{top:880px;font-size:37px;font-weight:500;letter-spacing:.5px}
.welcome p{position:absolute;left:400px;width:400px;text-align:center;font-size:12px;line-height:19.5px;color:#d6d8e2}
/* what we do */
.sec-title{font-size:37px;font-weight:600;color:var(--navy);letter-spacing:.3px}
.intro{font-size:12px;line-height:22px;color:var(--muted)}
.photo{position:absolute}
.svc-icon{position:absolute;width:56px;height:56px;border-radius:50%;background:#fbe3e3;display:flex;align-items:center;justify-content:center}
.svc-title{position:absolute;font-size:17px;font-weight:500;color:var(--navy);line-height:21px;width:300px}
.svc-text{position:absolute;font-size:11.5px;line-height:19px;color:var(--muted);width:290px}
.learn{position:absolute;font-size:12.5px;font-weight:600;color:var(--red)}
/* bio */
.bio-bg{position:absolute;left:0;top:2824px;width:1200px;height:529px;background:var(--soft)}
.bio-title{position:absolute;left:684px;top:2893px;font-size:34px;font-weight:600;line-height:41px;color:var(--navy)}
.bio p{position:absolute;left:682px;width:300px;font-size:11.5px;line-height:20.5px;color:var(--muted)}
.bio .quote{font-style:italic;font-weight:500;color:var(--navy)}
/* blog */
.card{position:absolute;top:3561px;width:256px;text-align:center}
.card .img{width:256px;height:182px}
.card h4{margin-top:22px;font-size:14.5px;font-weight:500;color:var(--navy)}
.card .date{font-size:10.5px;color:var(--red);margin-top:2px}
.card p{font-size:11px;line-height:19.5px;color:var(--muted);margin:14px 8px 0}
.card .btn{position:relative;margin:10px auto 0;width:134px;height:36px;font-size:13px}
.arrow-nav{position:absolute;top:3636px;font-size:30px;color:var(--navy);font-weight:300}
/* contact */
.form-card{position:absolute;left:195px;top:4032px;width:392px;height:472px;background:var(--white);box-shadow:0 4px 26px rgba(30,35,60,.12);z-index:2}
.form-card h3{position:absolute;top:44px;left:0;width:392px;text-align:center;font-size:18px;font-weight:500;line-height:27px;color:var(--navy)}
.field{position:absolute;left:41px;width:308px;height:35px;border:1px solid var(--line);font-size:10px;color:#9a9ca6;padding:10px 15px}
.field.first{border-color:var(--red);color:var(--red)}
.info h5{position:absolute;left:659px;top:4058px;font-size:14px;font-weight:500;color:var(--red)}
.info-icon{position:absolute;left:655px;width:36px;height:36px;border-radius:50%;border:1px solid var(--red);display:flex;align-items:center;justify-content:center}
.info .txt{position:absolute;left:705px;font-size:11px;color:var(--muted);line-height:19px}
.footer-brand{position:absolute;left:904px;top:4396px;display:flex;align-items:center;gap:8px;font-weight:700;font-size:19px;color:var(--white)}
.footer-brand .mark{width:14px;height:14px;background:var(--red)}
.copy{position:absolute;left:700px;width:340px;text-align:right;top:4477px;font-size:10px;color:#d6d8e2}
</style>
</head>
<body>

<!-- header -->
<div class="brand"><span class="mark"></span>Northwell Strategy</div>
<nav class="nav"><span class="active">HOME</span><span>ABOUT COMPANY</span><span>TEAM</span><span>WHAT WE DO</span><span>CONTACT US</span></nav>
<div class="call">
  <svg width="32" height="32" viewBox="0 0 32 32"><circle cx="16" cy="16" r="15" fill="none" stroke="#e3262a" stroke-width="1.5"/><path d="M11 9l3 0 1.5 4-2 1.5a9 9 0 0 0 4 4l1.5-2 4 1.5 0 3a2 2 0 0 1-2 2A13 13 0 0 1 9 11a2 2 0 0 1 2-2z" fill="#e3262a"/></svg>
  <div><small>Call Us On :</small><b>555-014-2290</b></div>
</div>

<!-- hero -->
<svg class="abs" style="left:0;top:0" width="1200" height="1227" viewBox="0 0 1200 1227">
  <polygon points="285,628 600,548 960,760 620,700" fill="#e3262a"/>
  <polygon points="0,706 222,594 700,690 1200,762 1200,1227 0,1227" fill="#262c4c"/>
</svg>
<div class="meeting" role="img" aria-label="Top-down view of four business people meeting around a table in red chairs"></div>
<div class="abs center hero-kicker">We Are Expert In</div>
<h1 class="abs center hero-title">IT &amp; CONSULTING<br>PROJECT MANAGEMENT</h1>
<div class="abs center hero-sub">We help you Scale your Business Operations to Become highly Profitable.</div>
<div class="btn" style="left:525px;top:329px;width:149px;height:37px">GET STARTED</div>
<div class="socials"><i></i><i></i><i></i></div>
<div class="dashes"><i></i><i></i><i></i><i></i></div>

<div class="welcome">
  <div class="abs center to">Welcome To</div>
  <div class="abs center name">NORTHWELL <span class="red">STRATEGY</span></div>
  <p style="top:942px">We are a specialist operational excellence firm, delivering consulting and advisory services in six core capabilities, across all industries and all business lines to improve performance, efficiency, profitability, automation and scalability, for clients across Australia.</p>
  <p style="top:1054px">We're known for our pragmatism, in depth analysis, strategic insight &amp; nurturing longterm client self sufficiency.</p>
</div>
<div class="btn" style="left:525px;top:1111px;width:149px;height:38px">LEARN MORE</div>

<!-- what we do -->
<h2 class="abs sec-title" style="left:243px;top:1294px">WHAT <span class="red">WE DO</span></h2>
<p class="abs intro" style="left:247px;top:1350px;width:500px">We offer first-class, Strategic and Financial insights that help you simplify and structure your processes to become a lean Efficient Enterprise.</p>

<div class="photo" style="left:252px;top:1430px;width:336px;height:316px;background:linear-gradient(135deg,#1f6fc0,#0c2a5c)" role="img" aria-label="Digital healthcare icons on a blue background"></div>
<div class="svc-icon" style="left:644px;top:1436px"><svg width="26" height="22" viewBox="0 0 26 22"><rect x="1" y="1" width="24" height="16" fill="none" stroke="#e3262a" stroke-width="1.5"/><path d="M5 10h4l2-4 3 7 2-3h5M9 21h8" fill="none" stroke="#e3262a" stroke-width="1.5"/></svg></div>
<div class="svc-title" style="left:644px;top:1500px">Market Entry</div>
<div class="svc-text" style="left:644px;top:1530px">Lorem Ipsum is simply dummy text of the printing and typesetting industry.</div>
<div class="learn" style="left:644px;top:1576px">Learn More →</div>

<div class="photo" style="left:642px;top:1625px;width:336px;height:316px;background:linear-gradient(135deg,#4f6a8c,#17233b)" role="img" aria-label="Hand holding a smartphone over financial charts"></div>
<div class="svc-icon" style="left:252px;top:1771px"><svg width="24" height="24" viewBox="0 0 24 24"><rect x="2" y="2" width="20" height="20" fill="none" stroke="#e3262a" stroke-width="1.5"/><path d="M6 16v-4M10 16v-7M14 16v-5M18 16V6" stroke="#e3262a" stroke-width="1.5"/></svg></div>
<div class="svc-title" style="left:252px;top:1836px">Technology Ananlysis Within Healthcare</div>
<div class="svc-text" style="left:252px;top:1889px">Lorem Ipsum is simply dummy text of the printing and typesetting industry.</div>
<div class="learn" style="left:252px;top:1935px">Learn More →</div>

<div class="photo" style="left:252px;top:1987px;width:336px;height:314px;background:linear-gradient(135deg,#e8484a,#c22327)" role="img" aria-label="Two colleagues reviewing documents, red tinted"></div>
<div class="svc-icon" style="left:644px;top:1970px"><svg width="26" height="26" viewBox="0 0 26 26"><circle cx="9" cy="17" r="6" fill="none" stroke="#e3262a" stroke-width="1.5"/><path d="M14 12l9-9M17 3h6v6" fill="none" stroke="#e3262a" stroke-width="1.5"/></svg></div>
<div class="svc-title" style="left:644px;top:2037px">Process Improvement within government</div>
<div class="svc-text" style="left:644px;top:2083px">Lorem Ipsum is simply dummy text of the.</div>
<div class="learn" style="left:644px;top:2107px">Learn More →</div>

<div class="photo" style="left:642px;top:2161px;width:336px;height:315px;background:linear-gradient(135deg,#1e5fa8,#0a1a3c)" role="img" aria-label="Blue stock market chart with candles"></div>
<div class="svc-icon" style="left:252px;top:2326px"><svg width="26" height="26" viewBox="0 0 26 26"><path d="M4 22l5-5M8 18c2-8 8-14 16-16-2 8-8 14-16 16zM17 9a1.5 1.5 0 1 0 .01 0" fill="none" stroke="#e3262a" stroke-width="1.5"/></svg></div>
<div class="svc-title" style="left:252px;top:2399px">Advise For Early Stage Startup</div>
<div class="svc-text" style="left:252px;top:2428px">Lorem Ipsum is simply dummy text of the printing and typesetting industry.</div>
<div class="learn" style="left:252px;top:2474px">Learn More →</div>

<div class="abs center" style="top:2630px;font-size:21px;font-weight:500;line-height:32px;color:var(--navy)">We help You Scale your Business Operations<br>to Become Highly Profitable.</div>
<div class="btn" style="left:507px;top:2710px;width:186px;height:38px;font-weight:500;font-size:15px;justify-content:flex-start;padding-left:44px">
  <svg class="abs" style="left:2px;top:2px" width="34" height="34" viewBox="0 0 34 34"><circle cx="17" cy="17" r="16" fill="#fff"/><path d="M12 10l3 0 1.5 4-2 1.5a9 9 0 0 0 4 4l1.5-2 4 1.5 0 3a2 2 0 0 1-2 2A13 13 0 0 1 10 12a2 2 0 0 1 2-2z" fill="#262c4c"/></svg>
  + 555 014 2290
</div>

<!-- bio -->
<section class="bio">
  <div class="bio-bg"></div>
  <div class="photo" style="left:275px;top:2880px;width:296px;height:473px;background:linear-gradient(180deg,#d9dbe0,#3b3f4c 45%,#2c2f3a)" role="img" aria-label="Portrait of a consultant in a dark suit with arms crossed"></div>
  <h2 class="bio-title">MARCUS<br><span class="red">ONDEKO BIO</span></h2>
  <p style="top:2994px">Marcus Ondeko is an IT professional with more than 20 years of experience turning business initiatives into technology solutions.</p>
  <p style="top:3067px">His expertise has been identifying deficiencies and developing or facilitating the best solutions for an outcome that is satisfactory to all stakeholders involved.</p>
  <p class="quote" style="top:3161px">Marcus improves business processes as older organizations restructure or migrate to newer technologies.</p>
  <div class="btn" style="left:681px;top:3238px;width:202px;height:38px;font-size:13px">MORE ABOUT MARCUS</div>
</section>

<!-- blog -->
<h2 class="abs center sec-title" style="top:3421px">LATEST <span class="red">BLOG</span></h2>
<p class="abs intro" style="left:390px;width:420px;top:3478px;text-align:center">Lorem Ipsum is simply text of the printing nturies, but also the leap into electronic typesetting remaining.</p>
<div class="arrow-nav" style="left:18px">‹</div>
<div class="arrow-nav" style="left:1166px">›</div>

<article class="card" style="left:53px"><div class="img" style="background:linear-gradient(135deg,#e65a5c,#c92a2e)" role="img" aria-label="Hands holding a phone, red tinted"></div><h4>Lorem Ipsum is Simply Text</h4><div class="date">12 Aug 2020 By Northwell</div><p>Lorem Ipsum is simply text of the printing nturies, but also the leap into electronic typesetting remaining.</p><div class="btn">LEARN MORE</div></article>
<article class="card" style="left:333px"><div class="img" style="background:linear-gradient(135deg,#eef1f5,#9aa3b0)" role="img" aria-label="Team gathered around a table in a bright office"></div><h4>Lorem Ipsum is Simply Text</h4><div class="date">12 Aug 2020 By Northwell</div><p>Lorem Ipsum is simply text of the printing nturies, but also the leap into electronic typesetting remaining.</p><div class="btn">LEARN MORE</div></article>
<article class="card" style="left:611px"><div class="img" style="background:linear-gradient(135deg,#6c7584,#2a303c)" role="img" aria-label="Business people shaking hands in an office"></div><h4>Lorem Ipsum is Simply Text</h4><div class="date">12 Aug 2020 By Northwell</div><p>Lorem Ipsum is simply text of the printing nturies, but also the leap into electronic typesetting remaining.</p><div class="btn">LEARN MORE</div></article>
<article class="card" style="left:892px"><div class="img" style="background:linear-gradient(135deg,#c9d3df,#6b7a8f)" role="img" aria-label="Colleagues working together at a laptop"></div><h4>Lorem Ipsum is Simply Text</h4><div class="date">12 Aug 2020 By Northwell</div><p>Lorem Ipsum is simply text of the printing nturies, but also the leap into electronic typesetting remaining.</p><div class="btn">LEARN MORE</div></article>

<!-- footer bands -->
<svg class="abs" style="left:0;top:4280px" width="1200" height="283" viewBox="0 0 1200 283">
  <polygon points="587,150 824,10 1200,130 1200,200 587,200" fill="#e3262a"/>
  <polygon points="0,205 886,55 1200,110 1200,283 0,283" fill="#262c4c"/>
</svg>

<!-- contact -->
<form class="form-card">
  <h3>Have an Any Question Please<br>Contact Us Today !</h3>
  <div class="field first" style="top:117px">Your Name *</div>
  <div class="field" style="top:163px">Organization *</div>
  <div class="field" style="top:208px">Phone *</div>
  <div class="field" style="top:252px">Email *</div>
  <div class="field" style="top:295px;height:71px">Write us a Message *</div>
  <div class="btn" style="left:136px;top:381px;width:112px;height:36px;font-size:13px">SUBMIT</div>
</form>

<div class="info">
  <h5>CONTACT INFO</h5>
  <div class="info-icon" style="top:4094px"><svg width="14" height="18" viewBox="0 0 14 18"><path d="M7 17S1 10 1 7a6 6 0 0 1 12 0c0 3-6 10-6 10z" fill="none" stroke="#e3262a" stroke-width="1.5"/><circle cx="7" cy="7" r="2" fill="#e3262a"/></svg></div>
  <div class="txt" style="top:4094px"><b style="color:var(--navy);font-weight:600;font-size:10.5px">Northwell Strategy Consulting</b><br>101 - Lorem ipsum simple text<br>print type text industry.</div>
  <div class="info-icon" style="top:4163px"><svg width="16" height="16" viewBox="0 0 16 16"><path d="M3 1l3 0 1.5 4-2 1.5a8 8 0 0 0 4 4l1.5-2 4 1.5 0 3a2 2 0 0 1-2 2A13 13 0 0 1 1 3a2 2 0 0 1 2-2z" fill="#e3262a"/></svg></div>
  <div class="txt" style="top:4171px;font-size:14px;font-weight:500;color:var(--navy)">+(1) 555 014 2290</div>
  <div class="info-icon" style="top:4206px"><svg width="16" height="12" viewBox="0 0 16 12"><rect x="1" y="1" width="14" height="10" fill="none" stroke="#e3262a" stroke-width="1.5"/><path d="M1 1l7 6 7-6" fill="none" stroke="#e3262a" stroke-width="1.5"/></svg></div>
  <div class="txt" style="top:4215px">info@northwellstrategy.example</div>
</div>

<div class="footer-brand"><span class="mark"></span>Northwell Strategy</div>
<div class="socials" style="left:950px;top:4449px"><i style="background:var(--red)"></i><i></i><i></i></div>
<div class="copy">©<span class="red">Northwell Strategy Consulting</span> - 2020 All rights reserved.</div>

</body>
</html>
```